Oversized Post card design

Need a post card design for rebrand, old post card attached for reference but some new content logos and colors. Id like to see new designs please use the one i posted as a reference of the type of design we like

Requirements
Must have
• Pricing page should no longer have "metered" plans only unlimited with these:
• 1 User: $29.99
• 2-10: $24.99/user
• 11-49: $21.99/user
• 50+: Contact Us!
• Add Ons:
• Call Recording: Starting at $5/user
• Additional Local Numbers: $1.99/number
• Fax to email: Starting at $8/user
• Toll Free Numbers: 1.99/number plus usage

```html
<!DOCTYPE html>
<html lang="en">
<head>
<meta charset="UTF-8">
<title>Plans and Pricing</title>
<link href="https://fonts.googleapis.com/css2?family=Montserrat:wght@600;700;900&family=Open+Sans:wght@400;600;700&display=swap" rel="stylesheet">
<style>
  :root{
    --cyan:#35c1e0;
    --cyan-line:#8fd9ec;
    --purple:#6b2c8f;
    --ink:#161616;
    --paper:#ffffff;
  }
  *{box-sizing:border-box;margin:0;padding:0}
  html,body{width:1200px;height:775px;overflow:hidden;background:var(--paper)}
  .card{position:relative;width:1200px;height:775px;background:var(--paper);font-family:"Open Sans",sans-serif;color:var(--ink)}

  .headline{position:absolute;left:0;top:44px;width:1228px;text-align:center;font-family:"Montserrat",sans-serif;font-weight:900;font-size:76px;letter-spacing:1px;color:var(--cyan);text-shadow:-5px 5px 0 var(--purple)}

  .section-title{position:absolute;font-family:"Montserrat",sans-serif;font-weight:700;font-size:33px;letter-spacing:1.5px;color:var(--ink)}
  .seats-title{left:66px;top:166px}
  .addons-title{left:440px;top:172px}

  .tier{position:absolute;width:160px;height:204px;border:2px solid var(--purple);text-align:center;padding-top:22px}
  .tier svg{display:block;margin:0 auto;height:34px}
  .tier-name{font-size:25px;font-weight:600;margin-top:12px}
  .tier-price{font-size:29px;font-weight:700;color:var(--purple);margin-top:16px;line-height:1}
  .tier-price sup{font-size:15px;vertical-align:top;position:relative;top:2px}
  .tier-unit{font-size:25px;font-weight:700;color:var(--purple);margin-top:4px}
  .tier-contact{font-size:28px;font-weight:700;color:var(--purple);margin-top:20px}
  .t1{left:63px;top:222px}.t2{left:229px;top:222px}
  .t3{left:63px;top:437px}.t4{left:229px;top:437px}

  .addon{position:absolute;left:437px;height:50px;width:728px}
  .addon > *{position:absolute;top:0;height:50px;border-radius:4px;display:flex;align-items:center;font-size:25px;padding-left:14px}
  .icon{left:0;width:50px;padding:0!important;justify-content:center;background:var(--cyan)}
  .icon.outlined{background:var(--paper);border:1.5px solid var(--cyan-line)}
  .cell{border:1.5px solid var(--cyan-line);color:var(--cyan);background:var(--paper)}
  .cell.filled{background:var(--cyan);color:#fff;border-color:var(--cyan)}
  .cell b{font-weight:700}
  .cell sup{font-size:13px;margin-right:1px;position:relative;top:-4px}
  .r1{top:220px}.r2{top:282px}.r3{top:344px}.r4{top:406px}
  .c-label{left:61px;width:213px}
  .c-start{left:279px;width:213px}
  .c-price{left:503px;width:225px}
  .c-label-wide{left:62px;width:330px}
  .c-price-wide{left:402px;width:326px}

  .brand{position:absolute;left:860px;top:596px;display:flex;align-items:center;gap:18px}
  .brand-mark{width:44px;height:44px;background:var(--cyan)}
  .brand-name{font-family:"Montserrat",sans-serif;font-weight:700;font-size:50px;letter-spacing:3px;color:var(--purple)}

  .contact{position:absolute;top:697px;left:40px;right:36px;display:flex;justify-content:space-between;align-items:center;font-family:"Montserrat",sans-serif;font-weight:700;font-size:27px;color:var(--ink)}
  .contact span{display:flex;align-items:center;gap:6px}
  .contact svg{height:26px}
</style>
</head>
<body>
<main class="card">
  <h1 class="headline">PLANS AND PRICING</h1>

  <h2 class="section-title seats-title">UNLIMITES SEAT</h2>

  <div class="tier t1">
    <svg viewBox="0 0 40 40"><circle cx="20" cy="11" r="8" fill="#161616"/><path d="M6 40c0-11 6-17 14-17s14 6 14 17z" fill="#161616"/></svg>
    <p class="tier-name">1 User</p>
    <p class="tier-price">$29.<sup>99</sup></p>
  </div>
  <div class="tier t2">
    <svg viewBox="0 0 60 40"><g fill="#161616"><circle cx="13" cy="10" r="7"/><path d="M0 34c0-10 5-15 13-15s13 5 13 15z"/><circle cx="47" cy="10" r="7"/><path d="M34 34c0-10 5-15 13-15s13 5 13 15z"/><circle cx="30" cy="15" r="8" stroke="#fff" stroke-width="2"/><path d="M15 40c0-10 6-16 15-16s15 6 15 16z" stroke="#fff" stroke-width="2"/></g></svg>
    <p class="tier-name">2-10 User</p>
    <p class="tier-price">$24.<sup>99</sup></p>
    <p class="tier-unit">/user</p>
  </div>
  <div class="tier t3">
    <svg viewBox="0 0 60 40"><g fill="#161616"><circle cx="13" cy="10" r="7"/><path d="M0 34c0-10 5-15 13-15s13 5 13 15z"/><circle cx="47" cy="10" r="7"/><path d="M34 34c0-10 5-15 13-15s13 5 13 15z"/><circle cx="30" cy="15" r="8" stroke="#fff" stroke-width="2"/><path d="M15 40c0-10 6-16 15-16s15 6 15 16z" stroke="#fff" stroke-width="2"/></g></svg>
    <p class="tier-name">11-49 User</p>
    <p class="tier-price">$21.<sup>99</sup></p>
    <p class="tier-unit">/user</p>
  </div>
  <div class="tier t4">
    <svg viewBox="0 0 60 40"><g fill="#161616"><circle cx="13" cy="10" r="7"/><path d="M0 34c0-10 5-15 13-15s13 5 13 15z"/><circle cx="47" cy="10" r="7"/><path d="M34 34c0-10 5-15 13-15s13 5 13 15z"/><circle cx="30" cy="15" r="8" stroke="#fff" stroke-width="2"/><path d="M15 40c0-10 6-16 15-16s15 6 15 16z" stroke="#fff" stroke-width="2"/></g></svg>
    <p class="tier-name">50+ User</p>
    <p class="tier-contact">contact us</p>
  </div>

  <h2 class="section-title addons-title">ADD ONS:</h2>

  <div class="addon r1">
    <div class="icon"><svg width="26" height="34" viewBox="0 0 26 34" fill="none" stroke="#fff" stroke-width="2.2"><rect x="8" y="2" width="10" height="18" rx="5"/><path d="M3 14a10 10 0 0 0 20 0M13 24v7M7 32h12"/></svg></div>
    <div class="cell c-label">Call Recording</div>
    <div class="cell c-start">Starting at</div>
    <div class="cell filled c-price"><sup>$</sup><b>5.00</b>/user</div>
  </div>
  <div class="addon r2">
    <div class="icon outlined"><svg width="32" height="32" viewBox="0 0 24 24"><path d="M6.6 10.8a15 15 0 0 0 6.6 6.6l2.2-2.2c.3-.3.7-.4 1-.2 1.1.4 2.3.6 3.6.6.6 0 1 .4 1 1V20c0 .6-.4 1-1 1A17 17 0 0 1 3 4c0-.6.4-1 1-1h3.5c.6 0 1 .4 1 1 0 1.3.2 2.5.6 3.6.1.3 0 .7-.2 1z" fill="#35c1e0"/></svg></div>
    <div class="cell filled c-label-wide">Additional Local Numbers</div>
    <div class="cell c-price-wide"><sup>$</sup><b>1.99</b>/number</div>
  </div>
  <div class="addon r3">
    <div class="icon"><svg width="34" height="30" viewBox="0 0 34 30" fill="none" stroke="#fff" stroke-width="1.8"><rect x="2" y="10" width="9" height="18" rx="2"/><rect x="11" y="12" width="14" height="14"/><rect x="13" y="3" width="10" height="9"/><rect x="21" y="18" width="12" height="9" fill="#35c1e0"/><path d="M21 18l6 5 6-5"/></svg></div>
    <div class="cell c-label">Fax to email</div>
    <div class="cell c-start">Starting at</div>
    <div class="cell filled c-price"><sup>$</sup><b>8.00</b>/user</div>
  </div>
  <div class="addon r4">
    <div class="icon outlined"><svg width="34" height="30" viewBox="0 0 34 30" fill="#35c1e0"><path d="M2 10c4-6 26-6 30 0l-1 4h-6l-1-4c-3-1-10-1-14 0l-1 4H3z"/><path d="M9 14h16l5 14H4z"/><circle cx="17" cy="21" r="4" fill="#fff"/></svg></div>
    <div class="cell filled c-label-wide">Toll Free Numbers</div>
    <div class="cell c-price-wide"><sup>$</sup><b>1.99</b>/number plus usage</div>
  </div>

  <div class="brand">
    <span class="brand-mark"></span>
    <span class="brand-name">VOXARA</span>
  </div>

  <footer class="contact">
    <span><svg viewBox="0 0 24 24" fill="none" stroke="#161616" stroke-width="1.8"><circle cx="12" cy="12" r="10"/><ellipse cx="12" cy="12" rx="4.5" ry="10"/><path d="M2 12h20M4 6.5h16M4 17.5h16"/></svg>www.novalinkvoice.com</span>
    <span><svg viewBox="0 0 30 20" fill="none" stroke="#161616" stroke-width="2"><rect x="1" y="1" width="28" height="18"/><path d="M1 1l14 11L29 1"/></svg>sales@novalinkvoice.com</span>
    <span><svg viewBox="0 0 24 24"><path d="M6.6 10.8a15 15 0 0 0 6.6 6.6l2.2-2.2c.3-.3.7-.4 1-.2 1.1.4 2.3.6 3.6.6.6 0 1 .4 1 1V20c0 .6-.4 1-1 1A17 17 0 0 1 3 4c0-.6.4-1 1-1h3.5c.6 0 1 .4 1 1 0 1.3.2 2.5.6 3.6.1.3 0 .7-.2 1z" fill="#161616"/></svg>855.NOVALK1</span>
  </footer>
</main>
</body>
</html>
```